SOC audit and security advisory company

We are a small public accounting firm that specializes in SOC attestations for small to medium sized business throughout the U.S. Our business is much like consulting, but we form an opinion about their operational controls. We are looking for "relevance and with a hint of polished sophistication". Our logo colors are dark gray and red. Our existing site is www.tolvanpartners.com for detailed information. We would like to include some type of captcha if possible. This is an information only site.

Target Market(s)

Small to medium sized financial and IT audit companies that are innovative and flexible.

Industry/Entity Type

Auditing

Coding

Coded - Design and coding required

Number of Pages Required

4 page

Font styles to use
Sans Serif

Requirements
Must have
• Good flow and attention to the content.
Nice to have
• CAPTCHA for contact us page
Should not have
• Big Bold lines.
• Too many distractions.

```html
<!DOCTYPE html>
<html lang="en">
<head>
<meta charset="utf-8">
<title>Tolvan Partners — Audit &amp; Advisory</title>
<link rel="stylesheet" href="https://fonts.googleapis.com/css2?family=Open+Sans:wght@400;600&family=Roboto:wght@300;400;500&display=swap">
<style>
:root{
  --accent:#f05a28;
  --ink:#222;
  --text:#555;
  --muted:#999;
  --band:#e8e8e8;
  --field:#eeeeee;
  --white:#fff;
}
*{box-sizing:border-box;margin:0;padding:0}
html,body{width:1200px;height:2261px;overflow:hidden}
body{position:relative;background:var(--white);font-family:"Open Sans",Arial,sans-serif;color:var(--text)}
.abs{position:absolute}
.heading{font-family:"Roboto",Arial,sans-serif;font-weight:400;color:var(--ink)}
.accent{color:var(--accent)}
.outline-btn{position:absolute;border:1.5px solid var(--accent);color:var(--accent);font-family:"Roboto",Arial,sans-serif;font-size:18px;display:flex;align-items:center;justify-content:center;background:transparent;text-transform:uppercase}

/* hero */
.hero{left:0;top:0;width:1200px;height:657px;background:linear-gradient(100deg,#eef1f3 0%,#dfe4e8 38%,#c9d3dc 62%,#e7d4bd 78%,#eef0f2 100%)}
.brand{display:flex;align-items:center;gap:10px;font-family:"Roboto",Arial,sans-serif;font-weight:500;font-size:34px;color:#555}
.brand-dot{width:14px;height:14px;border-radius:50%;background:var(--accent)}
.header-brand{left:80px;top:30px}
.nav{left:0;top:41px;font-family:"Roboto",Arial,sans-serif;font-size:17px;color:var(--ink)}
.nav a{position:absolute;color:inherit;text-decoration:none;white-space:nowrap}
.nav a.active{color:var(--accent)}
.appointment{left:915px;top:26px;width:208px;height:51px;background:var(--accent);color:var(--white);font-family:"Roboto",Arial,sans-serif;font-size:17px;display:flex;align-items:center;justify-content:center}
.hero-title{left:78px;top:252px;font-size:51px;line-height:62px;color:#111;font-weight:400}
.hero-sub{left:78px;top:380px;font-size:24px;color:#111;font-family:"Roboto",Arial,sans-serif}

/* welcome */
.section-title{left:0;width:1200px;text-align:center;font-size:42px}
.welcome-text{left:230px;top:768px;width:740px;text-align:center;font-size:13px;line-height:22.6px}

/* services */
.services{left:0;top:1001px;width:1200px;height:521px;background:var(--band)}
.service{position:absolute;top:1132px;width:340px;text-align:center}
.service-icon{width:124px;height:124px;border:1.5px solid var(--accent);border-radius:50%;margin:0 auto;display:flex;align-items:center;justify-content:center}
.service-name{margin-top:25px;font-size:22px}
.service-text{margin-top:12px;font-size:13px;line-height:22.6px;padding:0 50px}

/* contact */
.field{position:absolute;background:var(--field);font-size:13px;color:var(--muted);padding:0 22px;display:flex;align-items:center}
.field.bordered{background:var(--white);border:1px solid #ccc}
.captcha{left:345px;top:1830px;width:104px;height:51px;background:linear-gradient(90deg,#b9b9b9,#a6a6a6,#c2c2c2)}
.submit{left:460px;top:1830px;width:624px;height:51px;font-size:24px}

/* footer */
.footer{left:0;top:1939px;width:1200px;height:322px;background:var(--band)}
.footer-head{position:absolute;top:1970px;display:flex;align-items:center;gap:12px;font-family:"Roboto",Arial,sans-serif;font-size:24px;color:var(--accent)}
.footer-text{font-size:13px;line-height:22px;color:var(--text)}
.footer-link{position:absolute;font-size:14px;color:var(--text)}
.footer-rule{left:80px;top:2210px;width:1043px;height:1px;background:#999}
.copyright{left:80px;top:2224px;font-size:14px;color:var(--text)}
.social{position:absolute;top:2226px;width:16px;height:16px;border-radius:50%;background:#444}
</style>
</head>
<body>

<!-- hero -->
<div class="abs hero" role="img" aria-label="Bright office photo with a smiling consultant working on a laptop and colleagues in the background"></div>
<div class="abs brand header-brand"><span class="brand-dot"></span>Tolvan</div>
<nav class="abs nav">
  <a class="active" style="left:398px">Home</a>
  <a style="left:490px">About Us</a>
  <a style="left:606px">Services</a>
  <a style="left:718px">Contact Us</a>
</nav>
<div class="abs appointment">MAKE APPOINTMENT</div>
<h1 class="abs heading hero-title">ARE YOU READY TO TAKE THE<br>NEXT STEP?</h1>
<p class="abs hero-sub">WE ARE THERE TO KEEP YOU ON THE RIGHT PATH</p>
<div class="outline-btn" style="left:78px;top:445px;width:207px;height:51px;font-size:17px">CONTACT US NOW</div>

<!-- welcome -->
<h2 class="abs heading section-title" style="top:702px">WELCOME TO <span class="accent">TOLVAN</span></h2>
<p class="abs welcome-text">Tolvan was established to provide boutique audit and advisory services to small to medium sized businesses.&nbsp; We know that every company is different.&nbsp; We take a consultitive approach to engaging our clients so they fully understand the process and get something more than just a report!&nbsp; Our clients gain knowledge!<br>Our mission is to educate and provide high quality services through long term client relationships.</p>
<div class="outline-btn" style="left:517px;top:886px;width:166px;height:52px">KNOW MORE</div>

<!-- services -->
<div class="abs services"></div>
<h2 class="abs heading section-title" style="top:1045px">OUR <span class="accent">SERVICES</span></h2>

<div class="service" style="left:59px">
  <div class="service-icon">
    <svg width="56" height="60" viewBox="0 0 56 60" fill="none" stroke="#f05a28" stroke-width="4"><rect x="6" y="8" width="34" height="46" rx="3"/><rect x="16" y="3" width="14" height="9" fill="#f05a28"/><circle cx="38" cy="40" r="12" fill="#fff"/><path d="M32 40l4 4 8-8"/></svg>
  </div>
  <div class="heading service-name">SOC Services</div>
  <p class="service-text">No hidden costs.&nbsp; All Tolvan services are fixed price so you can budget effectively and with peace of mind.</p>
</div>
<div class="service" style="left:430px">
  <div class="service-icon">
    <svg width="84" height="56" viewBox="0 0 84 56" fill="#f05a28"><path d="M2 14l14-10 12 14-14 10z"/><path d="M82 14L68 4 56 18l14 10z"/><path d="M18 20l14-10 10 4 10-4 14 10-20 24-6 4-6-4z"/></svg>
  </div>
  <div class="heading service-name">Professional Advisory</div>
  <p class="service-text">No hidden costs.&nbsp; All Tolvan services are fixed price so you can budget effectively and with peace of mind.</p>
</div>
<div class="service" style="left:796px">
  <div class="service-icon">
    <svg width="56" height="62" viewBox="0 0 56 62"><path d="M28 2L4 10v18c0 16 11 26 24 32 13-6 24-16 24-32V10z" fill="#f05a28"/><path d="M28 9L11 15v13c0 11 8 19 17 24 9-5 17-13 17-24V15z" fill="#fff"/><rect x="19" y="28" width="18" height="14" rx="2" fill="#f05a28"/><path d="M22 28v-4a6 6 0 0112 0v4" fill="none" stroke="#f05a28" stroke-width="3"/></svg>
  </div>
  <div class="heading service-name">IT Security</div>
  <p class="service-text">No hidden costs.&nbsp; All Tolvan services are fixed price so you can budget effectively and with peace of mind.</p>
</div>
<div class="outline-btn" style="left:146px;top:1408px;width:167px;height:51px">READ MORE</div>
<div class="outline-btn" style="left:517px;top:1408px;width:166px;height:51px">READ MORE</div>
<div class="outline-btn" style="left:890px;top:1408px;width:166px;height:51px">READ MORE</div>

<!-- contact -->
<h2 class="abs heading section-title" style="top:1568px">Contact <span class="accent">Us</span></h2>
<div class="field bordered" style="left:116px;top:1642px;width:333px;height:51px">Name</div>
<div class="field" style="left:116px;top:1705px;width:333px;height:51px">E - Mail</div>
<div class="field" style="left:116px;top:1767px;width:333px;height:51px">Subject</div>
<div class="field" style="left:116px;top:1830px;width:219px;height:51px">Verification Code</div>
<div class="abs captcha" role="img" aria-label="Distorted verification code image"></div>
<div class="field" style="left:460px;top:1642px;width:624px;height:176px;align-items:flex-start;padding-top:14px">Message</div>
<div class="outline-btn submit">SUBMIT</div>

<!-- footer -->
<div class="abs footer"></div>
<div class="footer-head" style="left:80px">
  <svg width="22" height="26" viewBox="0 0 22 26" fill="#f05a28"><rect x="9" y="0" width="4" height="26"/><path d="M2 4h17l3 3-3 3H2z"/><path d="M20 13H3l-3 3 3 3h17z"/></svg>Company Information
</div>
<div class="footer-head" style="left:436px">
  <svg width="26" height="26" viewBox="0 0 26 26" fill="none" stroke="#f05a28" stroke-width="2"><path d="M6 2l5 6-3 3c2 4 4 6 8 8l3-3 6 5-3 4C12 24 2 14 2 6z"/></svg>Contact information
</div>
<div class="footer-head" style="left:791px">
  <svg width="26" height="26" viewBox="0 0 26 26" fill="none" stroke="#f05a28" stroke-width="3"><rect x="2" y="2" width="12" height="12" rx="5"/><rect x="12" y="12" width="12" height="12" rx="5"/></svg>Useful Links
</div>

<div class="abs brand" style="left:80px;top:2045px;font-size:32px"><span class="brand-dot"></span>Tolvan</div>
<p class="abs footer-text" style="left:80px;top:2124px;width:300px">Tolvan was founded to put the consultation back into audit and professional services.</p>

<p class="abs footer-text" style="left:436px;top:2021px">Phone No. : <span class="accent">000 0000 000</span></p>
<p class="abs footer-text" style="left:436px;top:2063px">E-Mail Address :<br><span class="accent">info@tolvanpartners.com</span></p>
<p class="abs footer-text" style="left:436px;top:2125px">Web Address :<br><span class="accent">&nbsp;www.tolvanpartners.com</span></p>

<span class="footer-link accent" style="left:791px;top:2021px">&gt;&nbsp; Terms &amp; Conditions</span>
<span class="footer-link" style="left:791px;top:2063px">&gt;&nbsp; Disclaimer</span>
<span class="footer-link" style="left:791px;top:2104px">&gt;&nbsp; FAQ's</span>

<div class="abs footer-rule"></div>
<p class="abs copyright">© <span class="accent">Tolvan Partners, Inc.</span> - 2016 All rights reserved</p>
<span class="social" style="left:1003px;background:var(--accent)"></span>
<span class="social" style="left:1043px"></span>
<span class="social" style="left:1082px"></span>

</body>
</html>
```